Back Pain

Need a flyer similar to the attached draft. This is to be handed out to prospective patients. Note that Sketch Hive has already designed the logo. If you need a copy please contact me

```html
<!DOCTYPE html>
<html lang="en">
<head>
<meta charset="utf-8">
<title>Tech Neck Flyer</title>
<link rel="stylesheet" href="https://fonts.googleapis.com/css2?family=Bebas+Neue&family=Oswald:wght@400;500;600&family=Open+Sans:ital,wght@1,700&family=Roboto+Condensed:wght@700&family=Questrial&family=Montserrat:wght@600&display=swap">
<style>
  :root {
    --stage: #bac3c6;
    --yellow: #fff200;
    --navy: #1d3f7a;
    --blue: #1574c0;
    --green: #8cc63f;
    --dark-green: #0a6b3a;
    --pink: #e6197a;
    --orange: #f26522;
    --ink: #2a2a2a;
    --white: #ffffff;
  }
  * { box-sizing: border-box; margin: 0; padding: 0; }
  html, body { width: 1200px; height: 1200px; overflow: hidden; background: var(--stage); }
  .flyer {
    position: absolute; left: 240px; top: 91px; width: 720px; height: 1018px; overflow: hidden;
    background:
      linear-gradient(215deg, rgba(21,116,192,0.95) 0%, rgba(40,150,210,0.75) 22%, rgba(150,210,240,0.4) 42%, rgba(255,255,255,0) 62%),
      linear-gradient(180deg, #e4f4fc 0%, #cfe6f6 35%, #dfe0f2 55%, #ffffff 68%);
    box-shadow: 0 4px 14px rgba(0,0,0,0.25);
  }
  .abs { position: absolute; }
  .brand { left: 40px; top: 60px; width: 190px; display: flex; align-items: center; gap: 8px; }
  .brand-dot { width: 22px; height: 22px; border-radius: 50%; background: var(--blue); flex: none; }
  .brand-name { font-family: "Oswald", sans-serif; font-weight: 500; font-size: 21px; color: var(--blue); line-height: 1; white-space: nowrap; }
  .title {
    right: 42px; top: 30px; white-space: nowrap;
    font-family: "Bebas Neue", sans-serif; font-weight: 400; font-size: 132px; line-height: 1; color: var(--yellow);
    text-shadow: 6px 6px 0 var(--navy);
  }
  .figure {
    left: 43px; top: 160px; width: 185px; height: 690px;
    background: linear-gradient(180deg, #93258d 0%, #c3215a 45%, #ec1c24 75%);
    border-radius: 90px 90px 24px 24px;
  }
  .symptom {
    height: 35px; border-radius: 0 18px 18px 0; padding-left: 16px; white-space: nowrap;
    background: linear-gradient(90deg, var(--green) 0%, #3f9a7a 50%, var(--blue) 100%);
    font-family: "Bebas Neue", sans-serif; font-size: 30px; line-height: 37px; color: var(--white);
  }
  .chart-caption { left: 447px; top: 188px; font-family: "Bebas Neue", sans-serif; font-size: 22px; line-height: 19px; color: var(--white); }
  .bar {
    width: 31px; bottom: 651px;
    background: linear-gradient(180deg, var(--green) 0%, #3c9a8a 50%, var(--blue) 100%);
    font-family: "Bebas Neue", sans-serif; font-size: 28px; color: var(--white); text-align: center; line-height: 30px;
  }
  .bar span { position: absolute; left: -6px; right: -6px; top: 2px; }
  .bar.first { background: #3e86a8; }
  .head-art { left: 447px; top: 255px; width: 62px; height: 66px; background: #f2f4f6; border-radius: 32px 32px 10px 20px; }
  .degrees { top: 384px; font-family: "Oswald", sans-serif; font-size: 20px; color: var(--orange); width: 44px; text-align: center; }
  .axis-label { left: 447px; top: 408px; width: 206px; font-family: "Bebas Neue", sans-serif; font-size: 20px; color: #eef3fb; white-space: nowrap; }
  .y-label {
    left: 583px; top: 280px; width: 160px; transform: rotate(-90deg);
    font-family: "Roboto Condensed", sans-serif; font-weight: 700; font-size: 12.5px; color: var(--white); white-space: nowrap; text-align: center;
  }
  .pie { left: 385px; top: 469px; }
  .usage { left: 478px; top: 472px; font-family: "Oswald", sans-serif; color: var(--ink); line-height: 1.15; }
  .usage .small { font-size: 18px; }
  .usage .big { font-size: 25px; }
  .pitch { right: 42px; top: 590px; text-align: right; font-family: "Bebas Neue", sans-serif; font-weight: 400; }
  .pitch div { white-space: nowrap; }
  .pitch .l1 { font-size: 45px; line-height: 40px; height: 40px; }
  .pitch .l2 { font-size: 35px; line-height: 32px; height: 32px; }
  .pitch .l3 { font-size: 43px; line-height: 36px; height: 36px; }
  .pitch .l4 { font-size: 43px; line-height: 38px; height: 38px; }
  .pink { color: var(--pink); }
  .blue { color: var(--blue); }
  .doctor { right: 42px; top: 766px; text-align: right; color: #333; }
  .doctor .name { font-family: "Open Sans", sans-serif; font-style: italic; font-weight: 700; font-size: 23px; letter-spacing: -0.6px; line-height: 30px; white-space: nowrap; }
  .doctor .addr { font-family: "Roboto Condensed", sans-serif; font-weight: 700; font-size: 20px; line-height: 25px; white-space: nowrap; }
  .offer-shadow { left: 200px; top: 905px; width: 322px; height: 16px; background: linear-gradient(180deg, rgba(0,0,0,0.18), rgba(0,0,0,0)); clip-path: polygon(4% 0, 96% 0, 100% 100%, 0 100%); }
  .offer {
    left: 186px; top: 873px; width: 350px; height: 42px; border-radius: 21px;
    background: var(--pink); box-shadow: 0 5px 0 #9c0f4f;
    font-family: "Questrial", sans-serif; font-size: 25px; line-height: 42px; color: var(--white); text-align: center;
  }
  .booking { left: 0; right: 0; top: 942px; text-align: center; font-family: "Montserrat", sans-serif; font-weight: 600; font-size: 16.5px; letter-spacing: 0.6px; color: var(--dark-green); }
  .band {
    left: 0; right: 0; top: 966px; height: 52px;
    border-top: 4px solid var(--green);
    background: linear-gradient(90deg, var(--blue) 0%, var(--blue) 30%, var(--green) 100%);
    font-family: "Montserrat", sans-serif; font-weight: 600; font-size: 19px; letter-spacing: 6px; color: var(--yellow);
    text-align: center; line-height: 46px;
  }
</style>
</head>
<body>
<main class="flyer">
  <div class="abs brand"><span class="brand-dot"></span><span class="brand-name">SPINE EASE CLINIC</span></div>
  <h1 class="abs title">TECH NECK</h1>

  <div class="abs figure" role="img" aria-label="Silhouette of a person walking while looking down at a phone, fading purple to red"></div>

  <div class="abs symptom" style="left:217px;top:181px;width:149px;">HEADACHES</div>
  <div class="abs symptom" style="left:199px;top:228px;width:134px;">NECKPAIN</div>
  <div class="abs symptom" style="left:189px;top:275px;width:188px;">SHOULDER PAIN</div>
  <div class="abs symptom" style="left:193px;top:322px;width:137px;">BACK PAIN</div>
  <div class="abs symptom" style="left:193px;top:405px;width:209px;">ARM &amp; HAND PAIN</div>
  <div class="abs symptom" style="left:199px;top:452px;width:119px;">SCIATICA</div>

  <p class="abs chart-caption">AS THE HEAD TILTS FORWARD.<br>MORE FORCE IS PLACED<br>ON THE SPINE</p>
  <div class="abs bar first" style="left:447px;height:25px;"><span>12</span></div>
  <div class="abs bar" style="left:491px;height:70px;"><span style="top:22px">27</span></div>
  <div class="abs bar" style="left:535px;height:106px;"><span style="top:34px">40</span></div>
  <div class="abs bar" style="left:578px;height:129px;"><span style="top:34px">49</span></div>
  <div class="abs bar" style="left:622px;height:158px;"><span style="top:42px">60</span></div>
  <div class="abs head-art" role="img" aria-label="Side profile outline of a head tilting forward"></div>
  <div class="abs degrees" style="left:440px;">0°</div>
  <div class="abs degrees" style="left:484px;">15°</div>
  <div class="abs degrees" style="left:528px;">30°</div>
  <div class="abs degrees" style="left:571px;">45°</div>
  <div class="abs degrees" style="left:615px;">60°</div>
  <div class="abs axis-label">DEGREES OF FORWARD HEAD TILT</div>
  <div class="abs y-label">PRESSURE ON SPINE (LBS)</div>

  <svg class="abs pie" width="86" height="86" viewBox="0 0 86 86" aria-hidden="true">
    <circle cx="43" cy="43" r="42" fill="#9acd6a"/>
    <path d="M43 43 L43 1 A42 42 0 0 1 67 77 Z" fill="#1574c0"/>
  </svg>
  <div class="abs usage">
    <div class="small">THE AVERAGE PERSON SPENDS</div>
    <div class="big">8-11 HOURS PER DAY</div>
    <div class="small">USING ELECTRONIC DEVICES</div>
  </div>

  <div class="abs pitch">
    <div class="l1"><span class="pink">CHIROPRACTIC CARE</span> <span class="blue">CAN HELP</span></div>
    <div class="l2 blue">CORRECT AND PREVENT THESE PROBLEMS</div>
    <div class="l3"><span class="blue">BY</span> <span class="pink">RESTORING</span> <span class="blue">AND</span> <span class="pink">MAINTAINING</span></div>
    <div class="l4"><span class="pink">PROPER ALIGNMENT</span> <span class="blue">OF THE NECK</span></div>
  </div>

  <div class="abs doctor">
    <div class="name">DR. BENJAMIN HARLOW</div>
    <div class="addr">NOW IN COASTVIEW AT</div>
    <div class="addr">42 HARBOUR RD - QUAY SUITES</div>
  </div>

  <div class="abs offer-shadow"></div>
  <div class="abs offer">50% Off Initial Consultation</div>
  <p class="abs booking">IF YOU BOOK ONLINE AT WWW.SPINEEASECLINIC.COM.AU</p>
  <div class="abs band">*CHOOSE “TECH NECK” OPTION</div>
</main>
</body>
</html>
```